Plakate für Laien-Chor
Es wurde sehr schnell und gut auf unsere Wünsche eingegangen.
Zielgruppe
Der Hallberg Chor Stuttgart ist ein gemischter Laien-Chor der Hallberg Musikgemeinschaft e.V. mit Verbundenheit zur Velotrax AG und Hallberg Nutzfahrzeuge AG. Im Herbst werden wir ein Konzert in der Marienkapelle Bad Cannstatt (Stuttgart) im Rahmen einer Spendereihe für den guten Zweck geben und benötigen dazu ein Plakat zu Werbezwecken (gedruckt als Poster (A3) und im Flyer-Format als auch digital für Homepage, Social Media etc.). Wir singen geistliche Lieder, die aber alle einen modernen Bezug haben. Das Thema Frieden soll sich im Plakat wiederspiegeln.
Aufgabenstellung
Konzert des Hallberg Chor Stuttgart
Der Titel des Konzertes ist: 'Songs of the Still Hour'
Musikalische Leitung: Britta Kolwe
Orgel: Marisol Adriana Fuentes Ortega
Eckdaten:
- Termin: Sonntag, 22.10.2023, Beginn: 18:00 Uhr (Einlass um 17:30 Uhr)
- Veranstaltungsort: Marienkapelle Bad Cannstatt
- Ticketvorverkauf über: https://tickets.chor-hmv.example (gerne auch als QR Code)
- Der Erlös kommt der Renovierung der Marienkapelle Bad Cannstatt und der Aktion 'Wintersterne in Cannstatt' zu Gute.
- Unser Hallberg Chor Logo, das Logo der Marienkapelle Bad Cannstatt, die Hallberg Chor Homepage und der Ticketverkauf sollen auf dem Plakat erscheinen. Ebenso der Hinweis zum Spendenzweck.
- Design im Hochformat (DIN A3-A5) für Druck und digitale Verwendung (PDF)
- Bitte keine Verwendung vom Velotrax-Emblem etc (keine Markenrechte)

```html
<!DOCTYPE html>
<html lang="de">
<head>
<meta charset="utf-8">
<title>Songs of the Still Hour – Hallberg Chor Stuttgart</title>
<link rel="stylesheet" href="https://fonts.googleapis.com/css2?family=Open+Sans:wght@400;600;700&family=Pacifico&display=swap">
<style>
  :root {
    --page-bg: #ffffff;
    --backdrop-light: #b3b3b5;
    --backdrop-mid: #a9a9ad;
    --backdrop-warm: #b9a89e;
    --circle-violet: rgba(128, 100, 160, 0.88);
    --title-orange: #f29100;
    --text-light: #f2f2f2;
    --text-soft: #ececec;
    --text-dark: #1e1e1e;
    --badge-gold: #f5b335;
    --badge-slate: #5a9aa6;
    --logo-grey: #7b7f86;
  }
  html, body {
    margin: 0;
    width: 1200px;
    height: 1200px;
    overflow: hidden;
    background: var(--page-bg);
    font-family: "Open Sans", Arial, sans-serif;
  }
  .poster {
    position: absolute;
    left: 206px;
    top: 146px;
    width: 680px;
    height: 964px;
    overflow: hidden;
  }
  .poster-backdrop {
    position: absolute;
    inset: 0;
    background:
      radial-gradient(ellipse at 85% 12%, rgba(215, 170, 90, 0.35), transparent 40%),
      radial-gradient(ellipse at 10% 10%, rgba(190, 110, 80, 0.3), transparent 35%),
      radial-gradient(ellipse at 70% 78%, rgba(200, 120, 70, 0.28), transparent 30%),
      linear-gradient(180deg, var(--backdrop-light), var(--backdrop-mid) 60%, var(--backdrop-light));
  }
  .peace-circle {
    position: absolute;
    left: 0;
    top: 0;
  }
  .presenter {
    position: absolute;
    top: 22px;
    width: 100%;
    text-align: center;
    font-weight: 700;
    font-size: 18px;
    color: var(--text-soft);
    margin: 0;
  }
  .concert-title {
    position: absolute;
    left: 132px;
    top: 185px;
    margin: 0;
    font-family: "Pacifico", cursive;
    font-weight: 400;
    font-size: 92px;
    line-height: 122px;
    color: var(--title-orange);
  }
  .credits {
    position: absolute;
    left: 131px;
    top: 596px;
    margin: 0;
    font-size: 22px;
    line-height: 30px;
    color: var(--text-light);
  }
  .credits strong { font-weight: 700; }
  .event-details {
    position: absolute;
    top: 770px;
    width: 100%;
    text-align: center;
    margin: 0;
    font-size: 22px;
    line-height: 30px;
    color: var(--text-soft);
  }
  .tickets, .website {
    position: absolute;
    width: 100%;
    text-align: center;
    margin: 0;
    font-size: 15px;
    color: var(--text-dark);
  }
  .tickets { top: 858px; }
  .website { top: 936px; }
  .proceeds {
    position: absolute;
    top: 885px;
    width: 100%;
    text-align: center;
    margin: 0;
    font-size: 12.5px;
    line-height: 20px;
    font-weight: 600;
    color: var(--text-dark);
  }
  .venue-mark {
    position: absolute;
    left: 19px;
    top: 884px;
    width: 62px;
    height: 62px;
    display: flex;
    flex-direction: column;
    justify-content: flex-end;
    background: var(--badge-gold);
    box-sizing: border-box;
    padding: 4px;
    font-size: 8.5px;
    line-height: 10px;
    font-weight: 600;
    color: var(--text-dark);
  }
  .choir-mark {
    position: absolute;
    left: 536px;
    top: 924px;
    display: flex;
    align-items: center;
    gap: 6px;
    font-size: 11px;
    font-weight: 600;
    color: var(--logo-grey);
  }
  .choir-mark-square {
    width: 20px;
    height: 20px;
    background: var(--badge-slate);
  }
</style>
</head>
<body>
  <main class="poster">
    <div class="poster-backdrop" role="img" aria-label="Hintergrundbild: zarte Zweige und herbstliche Blattgerippe auf grauem Grund"></div>
    <svg class="peace-circle" width="680" height="964" viewBox="0 0 680 964" aria-hidden="true">
      <circle cx="340" cy="417" r="335" fill="var(--circle-violet)"/>
    </svg>

    <p class="presenter">Der Hallberg Chor Stuttgart präsentiert</p>

    <h1 class="concert-title">Songs of<br>the Still<br>Hour</h1>

    <p class="credits">
      Musikalische Leitung: <strong>Britta Kolwe</strong><br>
      Orgel: <strong>Marisol Adriana Fuentes Ortega</strong>
    </p>

    <p class="event-details">
      (Sonntag, 22.10.2023, Beginn: 18:00 Uhr (Einlass um 17:30 Uhr)<br>
      in der Marienkapelle Bad Cannstatt
    </p>

    <p class="tickets">Ticketvorverkauf über: https://tickets.chor-hmv.example</p>
    <p class="proceeds">
      Der Erlös kommt der Renovierung der Marienkapelle Bad Cannstatt<br>
      und der Aktion 'Wintersterne in Cannstatt' zu Gute.
    </p>
    <p class="website">https://chor.hallberg-musikgemeinschaft.example</p>

    <div class="venue-mark">Marienkapelle Bad Cannstatt</div>

    <div class="choir-mark">
      <span class="choir-mark-square"></span>
      <span>Hallberg Chor Stuttgart</span>
    </div>
  </main>
</body>
</html>
```